BriskTail Pet - Cat Snack Range Packaging Design

Cat Velvo is a tasty snack for pets that comes in 3 flavors: Salmon, Tuna, Chicken. Each pack has 5 sticks.

Designs are currently too "cartoon-ish"; looking to refresh design into a high-end, "professional" product.

Prefer to have black/dark background with different colors for each flavor, but also open to designers' own creative take, as long as product looks professional.

Can refer to cat food brand "Marlow Feline" and "Plim" photo attached for reference.
https://www.marlowfeline.example/us/cats/products/vet-products

Looking to expand the design concept in the future to a whole range of cat products, such as cat litter, dental chewing sticks, canned cat food, etc.

Target Market(s)

More premium, high-end pet owners

Colors

Designer to choose only greyscale colors for use in the design.

Requirements
Must have
• Professional look
Nice to have
• Design template that can be copied and used for various product ranges (cat snacks, cans, litter, etc)

```html
<!DOCTYPE html>
<html lang="en">
<head>
<meta charset="utf-8">
<title>BriskTail Pet – Cat Velvo Mini Pouch Range</title>
<link rel="stylesheet" href="https://fonts.googleapis.com/css2?family=Montserrat:wght@600;700&family=Patrick+Hand&display=swap">
<style>
  :root {
    --page: #ffffff;
    --pouch-dark: #231f20;
    --ink-light: #ffffff;
    --window: #ffffff;
    --chicken: #d4928a;
    --salmon: #29a8e0;
    --tuna: #13a096;
    --icon-ink: #2b2b2b;
    --photo-light: #9a9a9a;
    --photo-dark: #3a3a3a;
    --shadow: rgba(0, 0, 0, 0.45);
  }
  * { margin: 0; padding: 0; box-sizing: border-box; }
  html, body { width: 1200px; height: 1000px; overflow: hidden; background: var(--page); }
  .canvas { position: relative; width: 1200px; height: 1000px; background: var(--page); }
  .pouch {
    position: absolute; top: 147px; width: 366px; height: 708px;
    box-shadow: 8px 8px 10px var(--shadow);
  }
  .pouch--chicken { left: 30px;  --flavour: var(--chicken); }
  .pouch--salmon  { left: 424px; --flavour: var(--salmon); }
  .pouch--tuna    { left: 813px; --flavour: var(--tuna); }
  .pouch svg { display: block; width: 366px; height: 708px; }
  .pouch-body { fill: var(--pouch-dark); }
  .hang-hole { fill: var(--window); }
  .tear-line { stroke: #cfcfcf; stroke-width: 1; stroke-dasharray: 6 5; }
  .mascot-slot { fill: #e6e2dc; }
  .brand-name { font-family: "Montserrat", sans-serif; font-weight: 700; font-size: 20px; fill: var(--ink-light); }
  .product-name { font-family: "Montserrat", sans-serif; font-weight: 700; font-size: 40px; fill: var(--ink-light); letter-spacing: 1px; }
  .tagline { font-family: "Patrick Hand", cursive; font-size: 14px; fill: var(--ink-light); }
  .flavour-name { font-family: "Montserrat", sans-serif; font-weight: 600; font-size: 24px; fill: var(--flavour); letter-spacing: 0.5px; }
  .flavour-extra { font-family: "Patrick Hand", cursive; font-size: 15px; fill: var(--ink-light); }
  .window { fill: var(--window); }
  .flavour-band { fill: var(--flavour); }
  .cat-photo { fill: url(#catTone); }
  .badge-ring { fill: none; stroke: var(--ink-light); stroke-width: 2; }
  .badge-leaf { fill: none; stroke: var(--ink-light); stroke-width: 1.8; }
  .badge-label { font-family: "Montserrat", sans-serif; font-weight: 700; font-size: 10px; fill: var(--icon-ink); }
  .chicken-icon { fill: none; stroke: var(--icon-ink); stroke-width: 2; }
  .net-weight { font-family: "Montserrat", sans-serif; font-weight: 600; font-size: 10.5px; fill: var(--icon-ink); }
</style>
</head>
<body>
<svg width="0" height="0" style="position:absolute" aria-hidden="true">
  <defs>
    <linearGradient id="catTone" x1="0" y1="0" x2="0" y2="1">
      <stop offset="0" stop-color="#8d8d8d"/>
      <stop offset="0.6" stop-color="#5c5c5c"/>
      <stop offset="1" stop-color="#2e2e2e"/>
    </linearGradient>
  </defs>
</svg>

<main class="canvas">

  <section class="pouch pouch--chicken">
    <svg viewBox="0 0 366 708">
      <rect class="pouch-body" width="366" height="708"/>
      <ellipse class="hang-hole" cx="183" cy="27" rx="40" ry="9"/>
      <line class="tear-line" x1="0" y1="69" x2="366" y2="69"/>
      <circle class="mascot-slot" cx="183" cy="150" r="40" role="img" aria-label="Brand mascot mark"/>
      <text class="brand-name" x="183" y="214" text-anchor="middle">BriskTail Pet</text>
      <text class="product-name" x="183" y="272" text-anchor="middle">CAT VELVO</text>
      <text class="tagline" x="183" y="296" text-anchor="middle">HEALTHY, TASTY &amp; NATURAL!</text>
      <text class="flavour-name" x="183" y="340" text-anchor="middle">CHICKEN MINI POUCH</text>
      <text class="flavour-extra" x="183" y="364" text-anchor="middle">WITH EXTRA - ADDED CAT GRASS</text>
      <path class="window" d="M78 573 V412 Q78 390 100 390 H248 Q270 390 270 412 V573 Z"/>
      <path class="flavour-band" d="M0 575 C120 566 260 520 366 412 V708 H0 Z"/>
      <rect class="cat-photo" x="150" y="395" width="200" height="273" rx="60" role="img" aria-label="Photo of a sitting grey tabby cat"/>
      <circle class="badge-ring" cx="35" cy="624" r="16"/>
      <path class="badge-leaf" d="M28 632 C28 620 36 614 43 614 C43 624 38 632 28 632 Z M28 632 L38 621"/>
      <text class="badge-label" x="35" y="658" text-anchor="middle">NATURAL</text>
      <rect class="chicken-icon" x="90" y="600" width="56" height="56" rx="6" role="img" aria-label="Chicken outline icon"/>
      <text class="net-weight" x="20" y="683">NET: 75 G ( 15GX5)</text>
    </svg>
  </section>

  <section class="pouch pouch--salmon">
    <svg viewBox="0 0 366 708">
      <rect class="pouch-body" width="366" height="708"/>
      <ellipse class="hang-hole" cx="183" cy="27" rx="40" ry="9"/>
      <line class="tear-line" x1="0" y1="69" x2="366" y2="69"/>
      <circle class="mascot-slot" cx="183" cy="150" r="40" role="img" aria-label="Brand mascot mark"/>
      <text class="brand-name" x="183" y="214" text-anchor="middle">BriskTail Pet</text>
      <text class="product-name" x="183" y="272" text-anchor="middle">CAT VELVO</text>
      <text class="tagline" x="183" y="296" text-anchor="middle">HEALTHY, TASTY &amp; NATURAL!</text>
      <text class="flavour-name" x="183" y="340" text-anchor="middle">SALMON MINI POUCH</text>
      <text class="flavour-extra" x="183" y="364" text-anchor="middle">WITH EXTRA - ADDED OMEGA 3</text>
      <path class="window" d="M78 573 V412 Q78 390 100 390 H248 Q270 390 270 412 V573 Z"/>
      <path class="flavour-band" d="M0 575 C120 566 260 520 366 412 V708 H0 Z"/>
      <rect class="cat-photo" x="150" y="395" width="200" height="273" rx="60" role="img" aria-label="Photo of a sitting grey tabby cat"/>
      <circle class="badge-ring" cx="50" cy="624" r="16"/>
      <path class="badge-leaf" d="M43 632 C43 620 51 614 58 614 C58 624 53 632 43 632 Z M43 632 L53 621"/>
      <text class="badge-label" x="50" y="658" text-anchor="middle">NATURAL</text>
      <rect class="chicken-icon" x="95" y="600" width="56" height="56" rx="6" role="img" aria-label="Chicken outline icon"/>
      <text class="net-weight" x="18" y="683">NET: 75 G ( 15GX5)</text>
    </svg>
  </section>

  <section class="pouch pouch--tuna">
    <svg viewBox="0 0 366 708">
      <rect class="pouch-body" width="366" height="708"/>
      <ellipse class="hang-hole" cx="183" cy="27" rx="40" ry="9"/>
      <line class="tear-line" x1="0" y1="69" x2="366" y2="69"/>
      <circle class="mascot-slot" cx="183" cy="150" r="40" role="img" aria-label="Brand mascot mark"/>
      <text class="brand-name" x="183" y="214" text-anchor="middle">BriskTail Pet</text>
      <text class="product-name" x="183" y="272" text-anchor="middle">CAT VELVO</text>
      <text class="tagline" x="183" y="296" text-anchor="middle">HEALTHY, TASTY &amp; NATURAL!</text>
      <text class="flavour-name" x="183" y="340" text-anchor="middle">TUNA MINI POUCH</text>
      <text class="flavour-extra" x="183" y="364" text-anchor="middle">WITH EXTRA - ADDED CRAMBERRY</text>
      <path class="window" d="M78 573 V412 Q78 390 100 390 H248 Q270 390 270 412 V573 Z"/>
      <path class="flavour-band" d="M0 575 C120 566 260 520 366 412 V708 H0 Z"/>
      <rect class="cat-photo" x="150" y="395" width="200" height="273" rx="60" role="img" aria-label="Photo of a sitting grey tabby cat"/>
      <circle class="badge-ring" cx="50" cy="624" r="16"/>
      <path class="badge-leaf" d="M43 632 C43 620 51 614 58 614 C58 624 53 632 43 632 Z M43 632 L53 621"/>
      <text class="badge-label" x="50" y="658" text-anchor="middle">NATURAL</text>
      <rect class="chicken-icon" x="95" y="600" width="56" height="56" rx="6" role="img" aria-label="Chicken outline icon"/>
      <text class="net-weight" x="18" y="683">NET: 75 G ( 15GX5)</text>
    </svg>
  </section>

</main>
</body>
</html>
```